Advertisement Coaching practice

I need an advertisement (to be printed in newspaper). I have a coaching practice where I offer coaching, workshops family constellations and relationship therapy. The ad needs to express calmness, inspiration to transform but also not dull and boring. It would be great if you could use the colors from my logo into the ad.

Dimensions are: 13,04 cm Width x 9,72 cm Height.

I will add my previous self-made ad, my company logo, a portrait photo of myself and the text I want to add. Also my contact details should be visible as well.

Requirements
Nice to have
• I have updated the brief with a flyer that I had previously made by a designer. It would be a nice to have if the ad ties in with that. You can also look at my website at www.fernbrook.nu to see what colors I used there.

```html
<!DOCTYPE html>
<html lang="nl">
<head>
<meta charset="utf-8">
<title>Fernbrook – Coaching, familieopstellingen &amp; relatietherapie</title>
<link rel="stylesheet" href="https://fonts.googleapis.com/css2?family=Poppins:wght@400;500;700;800&display=swap">
<style>
  :root{
    --navy:#0d4a6d;
    --blue:#1f72a8;
    --ink:#111820;
    --gold:#af9443;
    --grey:#5a5a5a;
    --paper:#ffffff;
  }
  html,body{margin:0;padding:0;width:1200px;height:895px;overflow:hidden;background:var(--paper);}
  .ad{position:relative;width:1200px;height:895px;background:var(--paper);font-family:"Poppins",sans-serif;color:var(--ink);overflow:hidden;}
  .headline{position:absolute;left:50px;top:32px;margin:0;font-weight:500;font-size:46px;line-height:55px;letter-spacing:.5px;color:var(--navy);text-transform:uppercase;}
  .intro{position:absolute;left:46px;top:216px;width:615px;margin:0;font-size:27px;line-height:31px;}
  .offer-title{position:absolute;left:46px;top:333px;margin:0;font-size:23.5px;font-weight:400;color:var(--blue);text-transform:uppercase;letter-spacing:.3px;}
  .offer-list{position:absolute;left:46px;top:363px;width:625px;margin:0;padding:0;list-style:none;font-size:27px;line-height:31px;}
  .offer-list li{position:relative;padding-left:29px;}
  .offer-list li::before{content:"";position:absolute;left:0;top:8px;border-left:15px solid var(--blue);border-top:8px solid transparent;border-bottom:8px solid transparent;}
  .details{position:absolute;left:46px;top:518px;width:630px;margin:0;font-size:27px;line-height:31px;}
  .phone{position:absolute;left:47px;top:764px;display:flex;align-items:center;gap:22px;}
  .phone-number{font-size:36px;font-weight:800;color:var(--blue);letter-spacing:.5px;}
  .contact-row{position:absolute;left:52px;top:833px;display:flex;align-items:center;gap:14px;font-size:13.5px;font-weight:700;color:var(--blue);}
  .contact-row span{display:flex;align-items:center;gap:8px;}
  .brand{position:absolute;left:788px;top:50px;display:flex;align-items:center;gap:20px;}
  .brand-name{font-size:48px;font-weight:400;color:var(--grey);letter-spacing:.5px;line-height:1;}
  .portrait{position:absolute;left:742px;top:151px;width:386px;height:540px;border:8px solid var(--navy);border-radius:58px;overflow:hidden;background:linear-gradient(160deg,#4d4a45 0%,#6e6258 40%,#a9876f 62%,#c3cbd8 100%);}
  .shapes{position:absolute;left:0;top:0;}
  .name{position:absolute;left:828px;top:805px;font-size:32px;font-weight:400;color:var(--paper);letter-spacing:.5px;}
</style>
</head>
<body>
<main class="ad">
  <h1 class="headline">Coaching,<br>familieopstellingen<br>&amp; relatietherapie</h1>

  <p class="intro">Trauma’s en negatieve ervaringen vormen ons en blijven nog lang voelbaar. Ze kunnen groei of geluk in de weg staan.</p>

  <h2 class="offer-title">Ik ben Mirella en ondersteun je bij het:</h2>
  <ul class="offer-list">
    <li>Doorbreken van belemmerende patronen;</li>
    <li>Beter omgaan met conflicten;</li>
    <li>In gezonde verbinding met elkaar als koppel<br>of met anderen komen;</li>
  </ul>

  <p class="details">Maandelijks geef ik workshops familieop-<br>stellingen. Ook houd ik themasessies rond adoptie, moeder-dochterdynamiek of relaties. Ook bied ik individuele coaching, relatietherapie en retraites aan. Kijk op de website voor meer info of neem contact op en ontdek wat het beste bij jou past.</p>

  <div class="phone">
    <svg width="62" height="62" viewBox="0 0 62 62" aria-hidden="true">
      <circle cx="31" cy="31" r="28" fill="none" stroke="var(--blue)" stroke-width="4"/>
      <path d="M21 17c2-1 4 0 5 2l2 5c1 2 0 3-1 4l-2 2c2 4 5 7 9 9l2-2c1-1 3-2 4-1l5 2c2 1 3 3 2 5l-1 2c-2 3-6 4-10 2-8-4-14-10-18-18-2-4-1-8 2-10z" fill="var(--navy)"/>
    </svg>
    <span class="phone-number">06-12 34 56 78</span>
  </div>

  <div class="contact-row">
    <span>
      <svg width="28" height="18" viewBox="0 0 28 18" aria-hidden="true"><rect x="1" y="1" width="26" height="16" fill="none" stroke="var(--blue)" stroke-width="2"/><path d="M1 1l13 10L27 1M1 17l10-8M27 17l-10-8" fill="none" stroke="var(--blue)" stroke-width="2"/></svg>
      info@fernbrook.nu
    </span>
    <span>
      <svg width="24" height="24" viewBox="0 0 24 24" aria-hidden="true"><g fill="none" stroke="var(--blue)" stroke-width="1.6"><circle cx="12" cy="12" r="10.5"/><ellipse cx="12" cy="12" rx="4.5" ry="10.5"/><path d="M1.5 12h21M3.5 6.5h17M3.5 17.5h17M12 1.5v21"/></g></svg>
      www.fernbrook.nu
    </span>
  </div>

  <div class="brand">
    <svg width="72" height="72" viewBox="0 0 72 72" aria-hidden="true"><circle cx="36" cy="36" r="33" fill="none" stroke="var(--navy)" stroke-width="4"/></svg>
    <span class="brand-name">fernbrook</span>
  </div>

  <div class="portrait" role="img" aria-label="Portretfoto van Mirella Dastani, coach, buiten in een stadsomgeving"></div>

  <svg class="shapes" width="1200" height="895" viewBox="0 0 1200 895" aria-hidden="true">
    <polygon points="519,895 1200,498 1200,895" fill="var(--gold)"/>
    <line x1="1002" y1="646" x2="1200" y2="533" stroke="var(--paper)" stroke-width="2"/>
    <polygon points="601,811 983,561 1065,609 688,861" fill="var(--navy)"/>
    <polygon points="717,700 760,676 800,720 735,720" fill="var(--navy)"/>
    <polygon points="928,693 1123,575 1182,607 982,725" fill="var(--paper)"/>
    <line x1="800" y1="895" x2="838" y2="872" stroke="var(--paper)" stroke-width="2"/>
  </svg>

  <div class="name">Mirella Dastani</div>
</main>
</body>
</html>
```